Food Festival "Signature Cocktail" Booth Banner

Need a 3'x9'6" (36" tall x 114" wide) Outdoor Banner for a new "Signature Cocktail" booth at an outdoor food festival. Pellston Onion Jubilee is a non profit festival and the World Record largest Garlic Festival with average of 100K attendees over 3 days. Actual drink served will vary from year to year, but banner for the booth with be reused each year so it will be non drink specific. Banner needs to catch attendee's attention both at a quick glance and from a distance outdoors to drive traffic and sales to the booth. It will be mounted above the sales window of a 10x10 Festival Booth on PVC frame (see attached pic for reference). "Signature Cocktail" is required text along with it being identified as a Pellston Onion Jubilee booth either through use of attached logo (color can be modified) or "Pellston Onion Jubilee" text since we also have for profit competing vendors. Banner will be full color print. Idea concepts: Neon Sign, Art Deco elegant, reclaimed wood...but open to any concepts. Festival website: https://pellstononionjubilee.example

Target Market(s)

Food Festival Attendees

Font styles to use
Decorative
Script
Other font styles liked:
• Neon, heavy weight fonts, open.

Colors

Designer to choose colors to be used in the design.

Requirements
Must have
• "Signature Cocktail" and "Pellston Onion Jubilee" text or POJ Logo provided, colors and layout that stands out and easily identifiable and readable from a long distance with strong text
Nice to have
• Vibrant engaging background,, ties to Garlic
Should not have
• Clip art, generic text

```html
<!DOCTYPE html>
<html lang="en">
<head>
<meta charset="utf-8">
<title>Signature Cocktail – Pellston Onion Jubilee Booth Banner</title>
<link rel="stylesheet" href="https://fonts.googleapis.com/css2?family=Luckiest+Guy&display=swap">
<style>
  :root {
    --page: #8f8f8f;
    --night: #1a0a1e;
    --plum: #7a1f6e;
    --berry: #b5247f;
    --sky: #3f8fe0;
    --violet: #9a5ce8;
    --magenta: #d6379c;
    --coral: #c9524f;
    --amber: #a8641f;
    --gold: #7a5a12;
    --badge: #ffffff;
    --badge-ink: #c2188f;
    --silver-hi: #ffffff;
    --silver-mid: #d7d7da;
    --silver-lo: #a8a8ad;
    --edge-orange: #f2a12b;
    --edge-pink: #e8338f;
    --edge-blue: #2fa6ea;
    --edge-purple: #8a4fd8;
    --shadow: #0b0510;
  }
  * { margin: 0; padding: 0; box-sizing: border-box; }
  html, body {
    width: 1200px; height: 470px; overflow: hidden;
    background: var(--page);
  }
  .banner {
    position: relative;
    width: 1200px; height: 470px;
    overflow: hidden;
  }
  .banner-backdrop {
    position: absolute; inset: 0;
    background:
      radial-gradient(ellipse at 30% 20%, rgba(255,255,255,0.28), transparent 40%),
      radial-gradient(ellipse at 70% 30%, rgba(255,255,255,0.18), transparent 40%),
      linear-gradient(90deg,
        var(--night) 0%, var(--plum) 10%, var(--berry) 18%,
        var(--sky) 32%, var(--sky) 40%, var(--violet) 50%,
        var(--magenta) 60%, var(--magenta) 68%, var(--coral) 76%,
        var(--amber) 86%, var(--gold) 94%, var(--night) 100%);
  }
  .festival-badge {
    position: absolute;
    left: 78px; top: 150px;
    width: 234px; height: 234px;
    border-radius: 50%;
    background: var(--badge);
    display: flex; align-items: center; justify-content: center;
    text-align: center;
  }
  .festival-name {
    font-family: "Luckiest Guy", sans-serif;
    font-weight: 400;
    font-size: 38px;
    line-height: 1.05;
    color: var(--badge-ink);
  }
  .headline {
    position: absolute;
    left: 350px; top: 50px;
    width: 810px; height: 380px;
  }
  .headline-text {
    font-family: "Luckiest Guy", sans-serif;
    font-size: 165px;
  }
  .headline-shadow { fill: var(--shadow); stroke: var(--shadow); stroke-width: 10; }
  .headline-face { fill: url(#silver); stroke: url(#neon-edge); stroke-width: 5; paint-order: stroke; }
</style>
</head>
<body>
  <main class="banner">
    <div class="banner-backdrop" role="img" aria-label="Glowing dotted light pattern fading from magenta through blue and pink to amber"></div>

    <div class="festival-badge">
      <p class="festival-name">Pellston<br>Onion<br>Jubilee</p>
    </div>

    <svg class="headline" viewBox="0 0 810 380" aria-label="Signature Cocktail">
      <defs>
        <linearGradient id="silver" x1="0" y1="0" x2="0" y2="1">
          <stop offset="0" stop-color="var(--silver-mid)"/>
          <stop offset="0.45" stop-color="var(--silver-hi)"/>
          <stop offset="0.55" stop-color="var(--silver-lo)"/>
          <stop offset="1" stop-color="var(--silver-hi)"/>
        </linearGradient>
        <linearGradient id="neon-edge" x1="0" y1="0" x2="1" y2="0">
          <stop offset="0" stop-color="var(--edge-orange)"/>
          <stop offset="0.3" stop-color="var(--edge-pink)"/>
          <stop offset="0.6" stop-color="var(--edge-blue)"/>
          <stop offset="0.85" stop-color="var(--edge-purple)"/>
          <stop offset="1" stop-color="var(--edge-pink)"/>
        </linearGradient>
      </defs>
      <g class="headline-text">
        <text class="headline-shadow" x="18" y="170" textLength="790" lengthAdjust="spacingAndGlyphs">SIGNATURE</text>
        <text class="headline-face" x="10" y="162" textLength="790" lengthAdjust="spacingAndGlyphs">SIGNATURE</text>
        <text class="headline-shadow" x="30" y="358" textLength="740" lengthAdjust="spacingAndGlyphs">COCKTAIL</text>
        <text class="headline-face" x="22" y="350" textLength="740" lengthAdjust="spacingAndGlyphs">COCKTAIL</text>
      </g>
    </svg>
  </main>
</body>
</html>
```